Venture Capital Investment Firm

We are looking to overhaul our existing website (substantially), with only using the same logos (which we can provide).
We are an investment firm that focuses on making loans to late stage technology companies. Our site should ultimately look like other venture capital firms, and look modern and fresh. We have an existing website www.northvaleloan.com which this will be replacing, although we will be using a lot of the existing written content, and potentially the numbers of pages we will need, we are not wed to anything else. Please feel free to shoot any questions at any time and thank you in advance for your help!
Websites we like as examples:
https://www.tkbrandel.com/
https://www.emberwoodfunds.com/
Target Market(s)
Potential investors who will invest in our firm, as well as potentially companies that are looking to borrow money from us.

```html
<!DOCTYPE html>
<html lang="en">
<head>
<meta charset="utf-8">
<title>Northvale Capital</title>
<link rel="stylesheet" href="https://fonts.googleapis.com/css2?family=Lato:wght@400;700&family=Poppins:wght@600;700&family=Roboto:wght@400;500&display=swap">
<style>
:root{
  --navy:#08083f;
  --navy-soft:rgba(14,14,70,.88);
  --ink:#1d1d1d;
  --muted:#6b6b6b;
  --light:#f2f2f2;
  --grey:#ececec;
  --footer:#333333;
  --white:#ffffff;
  --red:#d93025;
  --blue:#1e7bc4;
}
*{box-sizing:border-box;margin:0;padding:0}
html,body{width:1200px;height:3312px;overflow:hidden}
body{position:relative;font-family:"Lato",sans-serif;color:var(--ink);background:var(--white)}
.abs{position:absolute}
a{color:inherit;text-decoration:none}

/* header */
.site-header{position:absolute;left:0;top:0;width:1200px;height:67px;background:var(--white);border-bottom:1px solid #ddd}
.brand{position:absolute;left:111px;top:12px;display:flex;align-items:center;gap:12px}
.brand-dot{width:40px;height:40px;border-radius:50%;background:var(--navy)}
.brand-name{font-family:"Lato",sans-serif;font-weight:700;font-size:26px;color:var(--navy);letter-spacing:.5px}
.nav{position:absolute;top:0;left:0}
.nav a{position:absolute;top:24px;font-size:14.5px;font-weight:700;color:var(--ink);white-space:nowrap}
.nav a.active{color:var(--navy)}
.nav a.active::after{content:"";position:absolute;left:0;right:0;bottom:-9px;height:3px;background:var(--navy)}
.nav a.investors{top:17px;left:990px;width:96px;height:33px;line-height:33px;text-align:center;background:var(--navy);color:var(--white)}

/* hero */
.hero{position:absolute;left:0;top:67px;width:1200px;height:559px;background:linear-gradient(110deg,#5d9dbe 0%,#3a7ea6 35%,#1e4f78 65%,#17304f 100%)}
.hero-title{position:absolute;left:111px;top:178px;font-family:"Poppins",sans-serif;font-weight:700;font-size:56px;color:var(--white);letter-spacing:.5px}
.hero-sub{position:absolute;left:112px;top:258px;width:440px;font-size:15.5px;line-height:26px;color:var(--white)}
.btn{display:flex;align-items:center;justify-content:center;gap:10px;background:var(--navy);color:var(--white);font-weight:700;font-size:16px;border-radius:22px}
.btn .arrow{width:15px;height:15px;border-radius:50%;background:var(--white);display:flex;align-items:center;justify-content:center}
.hero .btn{position:absolute;left:113px;top:321px;width:161px;height:40px}
.hero-arrow{position:absolute;top:262px;width:34px;height:34px;border-radius:50%;background:var(--white);display:flex;align-items:center;justify-content:center}

/* headings */
.section-title{font-family:"Poppins",sans-serif;font-weight:700;font-size:38px;color:#111;letter-spacing:.3px}

/* about */
.about-tile{position:absolute;background:linear-gradient(135deg,#c9d3dc,#8d9aa8)}
.about-text{position:absolute;left:655px;top:765px;width:436px;font-size:15px;line-height:25.8px;color:var(--muted);text-align:justify}
.about .btn{position:absolute;left:655px;top:988px;width:150px;height:40px}

/* strategy */
.strategy{position:absolute;left:0;top:1093px;width:1200px;height:481px;background:linear-gradient(180deg,#f5f5f5,#ececec)}
.card{position:absolute;top:138px;width:314px;height:262px;background:#e9e9e9;text-align:center;padding-top:24px}
.card.featured{background:var(--navy);color:var(--white)}
.card h3{margin-top:14px;font-size:18px;font-weight:700;letter-spacing:.2px}
.card p{margin:12px auto 0;width:280px;font-size:16px;line-height:29px;color:var(--muted)}
.card.featured p{color:var(--white)}

/* news */
.news-photo{position:absolute;background:linear-gradient(135deg,#cfd6dc,#8796a3)}
.news-overlay{position:absolute;left:217px;top:1879px;width:371px;height:198px;background:var(--navy-soft);color:var(--white);padding:22px 28px}
.news-overlay h4{font-size:16px;line-height:26px;font-weight:700}
.meta{display:flex;align-items:center;gap:10px}
.news-overlay .meta{margin-top:12px;font-size:15px}
.news-overlay p{margin-top:12px;font-size:15px;line-height:26px}
.news-side{position:absolute;left:599px;width:488px;height:169px;background:var(--white);box-shadow:0 0 6px rgba(0,0,0,.12)}
.news-side .news-body{position:absolute;left:206px;top:20px;width:274px}
.news-side h4{font-size:11.5px;line-height:22px;font-weight:700;color:#111}
.news-side .meta{margin-top:6px;font-size:12px;color:var(--muted)}
.news-side p{margin-top:8px;font-size:12px;line-height:26px;color:var(--muted)}

/* team */
.team{position:absolute;left:0;top:2158px;width:1200px;height:835px;background:var(--grey)}
.member{position:absolute;top:138px;width:240px;text-align:center}
.avatar{width:154px;height:154px;margin:0 auto;border-radius:50%;background:radial-gradient(circle at 50% 40%,#6a6a6a,#1a1a1a)}
.member h5{margin-top:20px;font-size:17px;font-weight:700;color:#222}
.member .role{margin-top:4px;font-size:9px;font-style:italic;color:#666;letter-spacing:.3px}
.dots{display:flex;justify-content:center;gap:6px;margin-top:10px}
.dots span{width:22px;height:22px;border-radius:50%}
.divider{position:absolute;top:146px;width:1px;height:204px;background:#cfcfcf}

/* contact */
.field{position:absolute;background:var(--white);border:1px solid #e0e0e0;font-size:16px;color:#666;padding:10px 9px}
.submit{position:absolute;left:109px;top:2904px;width:129px;height:40px;border-radius:20px;background:var(--navy);color:var(--white);font-weight:700;font-size:16px;display:flex;align-items:center;justify-content:center}
.info-icon{position:absolute;left:809px;width:46px;height:46px;border-radius:50%;border:1.5px solid var(--navy);display:flex;align-items:center;justify-content:center}
.info-text{position:absolute;left:885px;font-size:16.5px;line-height:26px;color:#555}

/* footer */
.site-footer{position:absolute;left:0;top:2993px;width:1200px;height:270px;background:var(--footer);font-family:"Roboto",sans-serif;color:var(--white)}
.f-col{position:absolute;top:52px}
.f-col h6{font-size:17.5px;font-weight:500;text-decoration:underline;text-underline-offset:3px;margin-bottom:10px}
.f-col li{list-style:none;font-size:16.5px;line-height:35px;display:flex;align-items:center;gap:14px}
.f-col li::before{content:"»";font-size:16px}
.bottom-bar{position:absolute;left:0;top:3263px;width:1200px;height:49px;background:var(--navy);color:var(--white);font-family:"Roboto",sans-serif}
.bottom-bar .copy{position:absolute;left:113px;top:15px;font-size:16.5px}
.bottom-bar .social{position:absolute;left:957px;top:10px;display:flex;gap:12px}
.bottom-bar .social span{width:28px;height:28px;border-radius:50%;background:var(--white)}
</style>
</head>
<body>

<header class="site-header">
  <div class="brand"><span class="brand-dot"></span><span class="brand-name">Northvale Capital</span></div>
  <nav class="nav">
    <a class="active" style="left:408px">HOME</a>
    <a style="left:505px">STRATEGY</a>
    <a style="left:617px">ABOUT US</a>
    <a style="left:729px">TEAM</a>
    <a style="left:809px">NEWS</a>
    <a style="left:891px">CONTACT</a>
    <a class="investors">INVESTORS</a>
  </nav>
</header>

<section class="hero" role="img" aria-label="Businessman in a suit drawing a rising glowing financial chart over blue data figures">
  <h1 class="hero-title">NORTHVALE</h1>
  <p class="hero-sub">We Are a Global Structured Credit Investment Firm Focused On The Healthcare and Technology Industries.</p>
  <a class="btn">GET STARTED <span class="arrow"><svg width="7" height="8" viewBox="0 0 7 8"><path d="M1 0l6 4-6 4z" fill="#08083f"/></svg></span></a>
  <span class="hero-arrow" style="left:36px"><svg width="12" height="14" viewBox="0 0 12 14"><path d="M9 1L3 7l6 6" stroke="#111" stroke-width="2" fill="none"/></svg></span>
  <span class="hero-arrow" style="left:1130px"><svg width="12" height="14" viewBox="0 0 12 14"><path d="M3 1l6 6-6 6" stroke="#111" stroke-width="2" fill="none"/></svg></span>
</section>

<section class="about">
  <div class="about-tile" style="left:336px;top:694px;width:193px;height:191px;border:3px solid #fff;box-shadow:0 0 5px rgba(0,0,0,.2)" role="img" aria-label="Two colleagues meeting at an office table"></div>
  <div class="about-tile" style="left:113px;top:741px;width:242px;height:144px" role="img" aria-label="Hands reviewing printed financial charts"></div>
  <div class="about-tile" style="left:186px;top:889px;width:169px;height:124px" role="img" aria-label="Laptop with analytics on a desk"></div>
  <div class="about-tile" style="left:360px;top:889px;width:136px;height:156px" role="img" aria-label="Business meeting video thumbnail"></div>
  <h2 class="section-title abs" style="left:655px;top:703px">ABOUT US</h2>
  <p class="about-text">Northvale Capital is a private investment firm unique in its dual focus on life science and technology credit opportunities. Our ambidextrous approach to investing reflects a broad recognition and appreciation for the critical role intellectual property plays in the successful commercialization of products. We apply our extensive industry expertise to assess the revenue visibility created by these assets and offer a range of creative financing solutions.</p>
  <a class="btn">READ MORE <span class="arrow"><svg width="7" height="8" viewBox="0 0 7 8"><path d="M1 0l6 4-6 4z" fill="#08083f"/></svg></span></a>
</section>

<section class="strategy">
  <h2 class="section-title abs" style="left:0;width:1200px;text-align:center;top:43px">STRATEGY</h2>
  <div class="card" style="left:111px">
    <svg width="54" height="54" viewBox="0 0 54 54" fill="none" stroke="#08083f" stroke-width="2"><circle cx="27" cy="27" r="11"/><path d="M27 16V6M27 38v10M16 27H6M38 27h10M19 19l-7-7M35 35l7 7M35 19l7-7M19 35l-7 7"/><circle cx="27" cy="5" r="2.5"/><circle cx="5" cy="27" r="2.5"/><circle cx="49" cy="27" r="2.5"/><circle cx="12" cy="12" r="2.5"/><circle cx="42" cy="42" r="2.5"/></svg>
    <h3>LIFE SCIENCES</h3>
    <p>We have a long track record of partnering with companies and investors that create and commercialize life science products.</p>
  </div>
  <div class="card featured" style="left:444px">
    <svg width="54" height="54" viewBox="0 0 54 54" fill="none" stroke="#fff" stroke-width="2"><path d="M16 40c-6-4-9-10-8-17 2-10 11-16 21-15 9 1 16 9 16 18 0 6-3 10-7 13v8H20v-7z"/><circle cx="27" cy="24" r="6"/><path d="M27 14v4M27 30v4M17 24h4M33 24h4"/></svg>
    <h3>TECHNOLOGY</h3>
    <p>We uniquely offer sizeable and flexible structured credit financing solutions to innovative technology companies.</p>
  </div>
  <div class="card" style="left:775px">
    <svg width="54" height="54" viewBox="0 0 54 54" fill="none" stroke="#08083f" stroke-width="2"><rect x="14" y="6" width="22" height="30" rx="2"/><path d="M19 14h12M19 20h12M19 26h8"/><circle cx="38" cy="12" r="6"/><path d="M8 48l8-10h14l8-6"/></svg>
    <h3>TRANSACTION TYPES</h3>
    <p>Northvale Capital's proven strategy focuses on identifying opportunities where demonstrated commercial success has established underlying.</p>
  </div>
</section>

<section class="news">
  <h2 class="section-title abs" style="left:0;width:1200px;text-align:center;top:1627px">LATEST NEWS</h2>
  <div class="news-photo" style="left:111px;top:1728px;width:477px;height:349px" role="img" aria-label="Businessman working with a calculator and laptop"></div>
  <div class="news-overlay">
    <h4>NORTHVALE CAPITAL COMPLETES STRUCTURED DEBT INVESTMENT IN BRIGHTQUILL</h4>
    <div class="meta"><span>▦ April 2018</span><span>|</span><span>◌ 2 Comments</span></div>
    <p>Sed ut perspiciatis unde omnis iste natus error sit voluptatem accusantium doloremque.</p>
  </div>
  <article class="news-side" style="top:1728px">
    <div class="news-photo" style="left:0;top:0;width:181px;height:169px" role="img" aria-label="Colleagues reviewing documents at a desk"></div>
    <div class="news-body">
      <h4>NORTHVALE CAPITAL COMPLETES $22,000,000 STRUCTURED DEBT INVESTMENT IN FERNLINE</h4>
      <div class="meta"><span>▦ Oct. 2016</span><span>|</span><span>◌ 2 Comments</span></div>
      <p>Sed ut perspiciatis unde omnis iste natus error sit voluptatem accusantium. doloremque.</p>
    </div>
  </article>
  <article class="news-side" style="top:1908px">
    <div class="news-photo" style="left:0;top:0;width:181px;height:169px" role="img" aria-label="Hands holding a tablet in an office"></div>
    <div class="news-body">
      <h4>HALVORN SEMICONDUCTOR ACQUIRED BY TESSELATE FOR $55,000,000</h4>
      <div class="meta"><span>▦ April 2016</span><span>|</span><span>◌ 2 Comments</span></div>
      <p>Sed ut perspiciatis unde omnis iste natus error sit voluptatem accusantium. doloremque.</p>
    </div>
  </article>
</section>

<section class="team">
  <h2 class="section-title abs" style="left:0;width:1200px;text-align:center;top:52px">OUR TEAM</h2>
  <div class="divider" style="left:444px"></div>
  <div class="divider" style="left:755px"></div>
  <div class="member" style="left:183px">
    <div class="avatar" role="img" aria-label="Portrait of Marcus Ellery"></div>
    <h5>MARCUS ELLERY</h5><div class="role">MANAGING PARTNER</div>
    <div class="dots"><span style="background:var(--red)"></span><span style="background:var(--blue)"></span></div>
  </div>
  <div class="member" style="left:482px">
    <div class="avatar" role="img" aria-label="Portrait of Daniel Okoro"></div>
    <h5>DANIEL OKORO</h5><div class="role">MANAGING PARTNER</div>
    <div class="dots"><span style="background:var(--red)"></span><span style="background:var(--blue)"></span></div>
  </div>
  <div class="member" style="left:806px">
    <div class="avatar" role="img" aria-label="Portrait of Peter Lindqvist"></div>
    <h5>PETER LINDQVIST</h5><div class="role">PARTNER</div>
    <div class="dots"><span style="background:var(--red)"></span><span style="background:var(--blue)"></span></div>
  </div>

  <h2 class="section-title abs" style="left:111px;top:460px">CONTACT US</h2>
</section>

<section class="contact">
  <div class="field" style="left:111px;top:2694px;width:275px;height:43px">First Name</div>
  <div class="field" style="left:399px;top:2694px;width:275px;height:43px">Last Name</div>
  <div class="field" style="left:111px;top:2753px;width:275px;height:43px">Email</div>
  <div class="field" style="left:399px;top:2753px;width:275px;height:43px">Phone No</div>
  <div class="field" style="left:111px;top:2811px;width:563px;height:77px">Message</div>
  <a class="submit">SUBMIT</a>

  <span class="info-icon" style="top:2687px"><svg width="18" height="22" viewBox="0 0 18 22" fill="none" stroke="#08083f" stroke-width="2"><path d="M9 21s7-7 7-12A7 7 0 0 0 2 9c0 5 7 12 7 12z"/><circle cx="9" cy="9" r="2.5"/></svg></span>
  <p class="info-text" style="top:2680px">1240 Harlow Street #310<br>Riverton, CA&nbsp; 94000</p>
  <span class="info-icon" style="top:2759px"><svg width="20" height="20" viewBox="0 0 20 20"><path d="M4 1l4 4-2 3c1 3 3 5 6 6l3-2 4 4-3 3C8 18 2 12 1 4z" fill="#08083f"/></svg></span>
  <p class="info-text" style="top:2769px">555 010 2748</p>
  <span class="info-icon" style="top:2831px"><svg width="20" height="16" viewBox="0 0 20 16" fill="none" stroke="#08083f" stroke-width="2"><rect x="1" y="1" width="18" height="14" rx="2"/><path d="M1 3l9 6 9-6"/></svg></span>
  <p class="info-text" style="top:2841px">inquiries@northvalecapital.com</p>
</section>

<footer class="site-footer">
  <div class="f-col" style="left:123px"><h6>QUICK LINKS</h6><ul><li>Home</li><li>About Us</li><li>Strategy</li><li>Services</li><li>Contact Us</li></ul></div>
  <div class="f-col" style="left:361px"><h6>OTHER LINKS</h6><ul><li>FAQ</li><li>Blog</li><li>Privacy Policy</li><li>Help</li><li>Terms &amp; Conditions</li></ul></div>
  <div class="f-col" style="left:610px"><h6>NEQUE PORRO</h6><ul><li>Voluptatem accusantium</li><li>Doloremque laudantium</li><li>Eaque ipsa</li><li>Quis autem vel</li></ul></div>
  <div class="f-col" style="left:885px"><h6>NAM LIBERO TEMPORE</h6><ul><li>Itaque earum</li><li>Lorem ipsum</li><li>Excepteur sint</li><li>Nemo enim</li><li>Quis autem vel</li></ul></div>
</footer>
<div class="bottom-bar">
  <span class="copy">© 2019 Northvale Capital. All Rights Reserved</span>
  <div class="social"><span></span><span></span><span></span></div>
</div>

</body>
</html>
```